Business Card Design

We need a new business card design for our company, Lumen Forge.

Our website: www.brightrow7.ca

We are open to all ideas, from professional to very creative.
Updates

Design update requests:

1. We would like to see some examples with "BrightRow7" instead of "Lumen Forge" as the company name.
2. Would like to see "Software | Web | Branding" included on the card somewhere as well.

Thanks.

We are really trying to express the nature of our business through our business card.  "Lumen" can be misconstrued for the health industry, so use of "BrightRow7" and the "Software | Web | Branding" slogan are key to understanding our business.

We have uploaded a new PSD which includes a monitor, tablet, and phone screen.  This represents the flexibility of web applications and is another tool we would like to see used on business cards.

We will be eliminating designs today and will await updated designs with these new specs.

Thank-you.

Industry/Entity Type

Business

Requirements
Must have
• Content:
First M. Last
Managing Partner
e. email@brightrow7.ca
p. 555.555.5555

```html
<!DOCTYPE html>
<html lang="en">
<head>
<meta charset="utf-8">
<title>BrightRow7 — Business Card</title>
<link href="https://fonts.googleapis.com/css2?family=Exo+2:ital,wght@0,300;0,400;0,600;1,300&display=swap" rel="stylesheet">
<style>
  :root {
    --page-bg: #e9eaeb;
    --card-bg: #ffffff;
    --ink-dark: #3b3d40;
    --ink-mid: #6a6d71;
    --ink-soft: #8d9095;
    --blue-deep: #1f6f9c;
    --blue-mid: #3a9fd3;
    --blue-light: #9fd6f0;
    --card-shadow: rgba(0, 0, 0, 0.12);
  }
  * { box-sizing: border-box; margin: 0; padding: 0; }
  html, body {
    width: 1200px;
    height: 2925px;
    overflow: hidden;
    background: var(--page-bg);
    font-family: "Exo 2", sans-serif;
    color: var(--ink-dark);
  }
  .canvas { position: relative; width: 1200px; height: 2925px; }

  .card {
    position: absolute;
    left: 60px;
    width: 1080px;
    height: 617px;
    background: var(--card-bg);
    overflow: hidden;
    box-shadow: 0 10px 30px var(--card-shadow);
  }
  .card--front { top: 745px; }
  .card--back { top: 1562px; }

  .pixel-field {
    position: absolute;
    background: radial-gradient(ellipse at center, var(--blue-mid) 0%, var(--blue-deep) 35%, var(--blue-light) 62%, rgba(159, 214, 240, 0) 72%);
  }
  .card--front .pixel-field { left: -170px; top: -210px; width: 560px; height: 540px; }
  .card--back .pixel-field { right: -160px; top: 90px; width: 460px; height: 470px; }

  .brand {
    position: absolute;
    display: flex;
    align-items: center;
    white-space: nowrap;
  }
  .brand__square { background: var(--blue-mid); flex: none; }
  .brand__text { display: flex; flex-direction: column; }
  .brand__name { color: var(--ink-dark); font-weight: 600; letter-spacing: 0.02em; line-height: 1.05; }
  .brand__slogan { color: var(--ink-mid); font-weight: 300; letter-spacing: 0.08em; }

  .card--front .brand { right: 110px; bottom: 150px; gap: 22px; }
  .card--front .brand__square { width: 70px; height: 70px; }
  .card--front .brand__name { font-size: 54px; }
  .card--front .brand__slogan { font-size: 19px; margin-top: 6px; }

  .card--back .brand { left: 70px; top: 56px; gap: 14px; }
  .card--back .brand__square { width: 42px; height: 42px; }
  .card--back .brand__name { font-size: 28px; }
  .card--back .brand__slogan { font-size: 12px; margin-top: 3px; }

  .person { position: absolute; left: 70px; top: 185px; }
  .person__name { font-size: 36px; font-weight: 400; color: var(--ink-dark); }
  .person__role { font-size: 20px; font-weight: 300; font-style: italic; color: var(--ink-mid); margin-top: 4px; }

  .contact { position: absolute; left: 70px; top: 310px; list-style: none; }
  .contact li { font-size: 20px; font-weight: 300; color: var(--ink-mid); line-height: 1.5; }

  .social-row {
    position: absolute;
    left: 70px;
    right: 70px;
    bottom: 36px;
    display: flex;
    justify-content: space-between;
    list-style: none;
  }
  .social-row li { display: flex; align-items: center; gap: 10px; font-size: 15px; font-weight: 300; color: var(--ink-soft); }
  .social-row__square { width: 18px; height: 18px; background: var(--blue-deep); }
</style>
</head>
<body>
<main class="canvas">

  <section class="card card--front" aria-label="Card front">
    <div class="pixel-field" role="img" aria-label="Decorative pattern of blue square tiles forming a large heart"></div>
    <div class="brand">
      <span class="brand__square"></span>
      <span class="brand__text">
        <span class="brand__name">BrightRow7</span>
        <span class="brand__slogan">Software | Web | Branding</span>
      </span>
    </div>
  </section>

  <section class="card card--back" aria-label="Card back">
    <div class="pixel-field" role="img" aria-label="Decorative pattern of blue square tiles forming a large heart"></div>
    <div class="brand">
      <span class="brand__square"></span>
      <span class="brand__text">
        <span class="brand__name">BrightRow7</span>
        <span class="brand__slogan">Software | Web | Branding</span>
      </span>
    </div>
    <div class="person">
      <p class="person__name">Jane R. Roe</p>
      <p class="person__role">Managing Partner</p>
    </div>
    <ul class="contact">
      <li>Your Street 123</li>
      <li>e. email@brightrow7.ca</li>
      <li>p. 555.555.5555</li>
      <li>www.brightrow7.ca</li>
    </ul>
    <ul class="social-row">
      <li><span class="social-row__square"></span>/brightrow7</li>
      <li><span class="social-row__square"></span>@brightrow7</li>
      <li><span class="social-row__square"></span>+brightrow7</li>
    </ul>
  </section>

</main>
</body>
</html>
```